Wedding Invitation to be used digitally

Design of a Wedding Invitation.
It will be used digitally by whatsapp, so the file format and image size should be appropriate. We don´t intend to print.
Word file with the text contents as attachment. This is REALLY just the text and the main sequencial order of the information that should appear in the invitation.
However, ALL criativity is welcome ofcourse in terms of organization of the information in the paper, font, uppercase and lowercase, numbers and their format, dates and their format, drawings, logo, etc etc

Target Market(s)

family and friends

Requirements
Must have
• A logo at the top with the capitals of our name - R and T
Nice to have
• Should be elegant

```html
<!DOCTYPE html>
<html lang="en">
<head>
<meta charset="utf-8">
<title>Wedding Invitation – Rosana &amp; Tiago</title>
<link href="https://fonts.googleapis.com/css2?family=Playfair+Display:wght@400&display=swap" rel="stylesheet">
<style>
  :root {
    --backdrop: #efebec;
    --paper: #ffffff;
    --ink: #2e2c2c;
    --gold: #9a8560;
    --gold-soft: #cbbb9c;
    --ampersand: #d8c9ab;
    --peony: #f6dfe8;
    --leaf: #e3e8dc;
  }
  * { box-sizing: border-box; margin: 0; padding: 0; }
  html, body {
    width: 1200px; height: 854px; overflow: hidden;
    background: var(--backdrop);
    font-family: "Playfair Display", Georgia, serif;
    font-weight: 400;
    color: var(--ink);
  }
  .invitation {
    position: absolute; left: 353px; top: 104px;
    width: 457px; height: 645px;
    background: var(--paper); overflow: hidden;
  }
  .floral { position: absolute; pointer-events: none; }
  .floral--top {
    left: -20px; top: -10px; width: 250px; height: 245px;
    background:
      radial-gradient(ellipse 45% 40% at 60% 30%, var(--peony) 0%, rgba(246,223,232,0.75) 55%, rgba(246,223,232,0) 100%),
      radial-gradient(ellipse 40% 45% at 35% 70%, var(--peony) 0%, rgba(246,223,232,0.6) 55%, rgba(246,223,232,0) 100%),
      radial-gradient(ellipse 55% 55% at 50% 50%, var(--leaf) 0%, rgba(227,232,220,0) 100%);
  }
  .floral--bottom {
    left: 220px; top: 405px; width: 250px; height: 250px;
    background:
      radial-gradient(ellipse 40% 35% at 45% 25%, var(--peony) 0%, rgba(246,223,232,0.7) 55%, rgba(246,223,232,0) 100%),
      radial-gradient(ellipse 40% 40% at 60% 65%, var(--peony) 0%, rgba(246,223,232,0.7) 55%, rgba(246,223,232,0) 100%),
      radial-gradient(ellipse 55% 60% at 55% 55%, var(--leaf) 0%, rgba(227,232,220,0) 100%);
  }
  .frame {
    position: absolute; left: 32px; top: 108px; width: 393px; height: 473px;
  }
  .frame svg { width: 100%; height: 100%; overflow: visible; display: block; }
  .monogram {
    position: absolute; left: 112px; top: 26px; width: 233px; height: 183px;
    display: flex; align-items: center; justify-content: center;
    font-size: 96px; line-height: 1; color: var(--gold); letter-spacing: 2px;
  }
  .line {
    position: absolute; left: 0; width: 100%;
    text-align: center; white-space: nowrap; font-weight: 400;
  }
  .lead   { top: 221px; font-size: 10.5px; line-height: 14px; letter-spacing: 1.9px; }
  .ampersand {
    top: 252px; font-size: 92px; line-height: 92px; color: var(--ampersand);
  }
  .name { font-size: 37px; line-height: 40px; letter-spacing: 0.3px; }
  .name--first  { top: 240px; }
  .name--second { top: 311px; }
  .invite { top: 365px; font-size: 10.5px; line-height: 14px; letter-spacing: 1.5px; }
  .divider {
    position: absolute; left: 198px; top: 397px; width: 61px; height: 1.5px;
    background: var(--gold);
  }
  .date { top: 414px; font-size: 15px; line-height: 18px; }
  .venue { font-size: 10.6px; line-height: 13px; }
  .venue--ceremony       { top: 462px; }
  .venue--reception-note { top: 500px; }
  .venue--reception      { top: 526px; }
  .rsvp {
    position: absolute; left: 26px; top: 605px;
    font-size: 10.5px; line-height: 14px; letter-spacing: 1.6px;
  }
</style>
</head>
<body>
  <main class="invitation">
    <div class="floral floral--top" role="img" aria-label="Soft pink peony bouquet with pale green leaves"></div>
    <div class="floral floral--bottom" role="img" aria-label="Soft pink peony bouquet with pale green leaves"></div>

    <div class="frame">
      <svg viewBox="0 0 393 473" preserveAspectRatio="none">
        <polyline points="120,0.5 0.5,0.5 0.5,472.5 392.5,472.5 392.5,0.5 286,0.5"
                  fill="none" stroke="var(--gold-soft)" stroke-width="1"/>
      </svg>
    </div>

    <div class="monogram">R&amp;T</div>

    <p class="line lead">TOGETHER WITH THEIR FAMILIES</p>
    <span class="line ampersand" aria-hidden="true">&amp;</span>
    <h1 class="line name name--first">ROSANA VELEZ</h1>
    <h1 class="line name name--second">TIAGO MOREIRA</h1>
    <p class="line invite">INVITE YOU TO THEIR WEDDING CELEBRATION</p>

    <div class="divider"></div>

    <p class="line date">SUNDAY, JULY 28, 2024<br>AT 11h30</p>

    <p class="line venue venue--ceremony">CAPELA DE SANTA LUZIA | VILA CLARA<br>(PARKING – MARINA DA VILA CLARA OR PARQUE TERRA MAR VILA CLARA)</p>
    <p class="line venue venue--reception-note">RECEPTION TO FOLLOW</p>
    <p class="line venue venue--reception">AT<br>HOTEL QUINTA DO FAROL | VILA CLARA<br>(PARKING – ON SITE)</p>

    <p class="rsvp">RSVP BY 20TH JULY</p>
  </main>
</body>
</html>
```